Graphics Design of Physics Book

Hi
Size : 8" x 11.25"
We are education book Publication Company and would like to have book cover for "Physics" it has 4 volumes. All 4 having the same color scheme and design except the volume no.
Blue is my personal favorite but u can use any color. Want to have a band at the bottom of the cover to place our Logo “VORLIN Education” a PDF of the same is attached, or you can place logo anywhere according to ur design.
I need “Physics” as title of the book to be visible prominently.
And volume and volume no. should also be Visible and eye catching I prefer a Graphic to enhance the Volume No.
A background pattern can also be a option (it should be vector form so that color can be change later)
Please do not offer any cut and paste design I need very professional presentation.
Volume and Number can be in metallic 3D (CMYK) effect.
only Professional presentation will get feedback.
I have provided a sample artwork for reference do not follow it but can be a reference what I needed !

Target Market(s)

Students Class 9th to 12th

Industry/Entity Type

Education

Font styles to use
Serif

Colors
3176b5
0555a3
85abd2
cadf82
abd036
9bcb3c

Requirements
Must have
• Eye catching.
• “Physics” as title of the book to be visible prominently.
• volume and volume no. should also be Visible and eye catching
• I prefer a Graphic to enhance the Volume No.
• Icons for
• 1. Questions and answers
• 2. Theory Notes
• 3. Tips & Tricks
• 4. Previous Year's Reference Questions
• 5. Covers Complete Syllabus
Nice to have
• decent seamless background or metallic 3d effect (not to be print in special Ink) design should only be in CMYK.
Should not have
• Physics related Pictures or Icons (Specially E=mc2) or any scientist photograph or I Need pure graphic design

```html
<!DOCTYPE html>
<html lang="en">
<head>
<meta charset="utf-8">
<title>Physics Volume 1 – Cover Options</title>
<link rel="stylesheet" href="https://fonts.googleapis.com/css2?family=Bodoni+Moda:wght@400;600&family=Questrial&family=Arimo&display=swap">
<style>
  :root {
    --page-bg: #ffffff;
    --frame: #1a1a1a;
    --ink: #000000;
    --paper: #ffffff;
    --teal-deep: #1f8db5;
    --teal-mid: #29a8cf;
    --teal-light: #46c9e6;
    --sky-pale: #bfe8f7;
    --sky-soft: #9fd9ef;
    --lime: #cdfa6a;
    --lime-band: #c8f55a;
    --cyan: #44e8ff;
    --title-cyan: #00ccff;
    --icon-dark: #0555a3;
  }
  html, body {
    margin: 0;
    padding: 0;
    width: 1200px;
    height: 968px;
    overflow: hidden;
    background: var(--page-bg);
  }
  .sheet {
    display: block;
    width: 1200px;
    height: 968px;
  }
  .sheet-frame { fill: none; stroke: var(--frame); stroke-width: 2; }
  .serif { font-family: "Bodoni Moda", "Times New Roman", serif; }
  .title-serif { fill: var(--paper); font-size: 104px; font-weight: 400; }
  .title-sans { font-family: "Questrial", "Century Gothic", sans-serif; fill: var(--title-cyan); font-size: 104px; }
  .volume-label { fill: var(--ink); font-weight: 600; }
  .bubble { fill: var(--lime); stroke: var(--paper); stroke-width: 10; }
  .bubble-white { fill: var(--paper); }
  .publisher { fill: var(--ink); font-family: "Bodoni Moda", "Times New Roman", serif; font-weight: 600; font-size: 26px; }
  .option-label { font-family: "Arimo", Arial, sans-serif; font-size: 50px; fill: var(--ink); }
  .band-lime { fill: var(--lime-band); }
  .band-cyan { fill: var(--cyan); }
  .feature-icon { fill: none; stroke-width: 2.6; stroke-linecap: round; stroke-linejoin: round; }
  .features-light { color: var(--paper); }
  .features-dark { color: var(--icon-dark); }
</style>
</head>
<body>
<svg class="sheet" viewBox="0 0 1403 1132" xmlns="http://www.w3.org/2000/svg">
  <defs>
    <linearGradient id="wash-teal" x1="0" y1="0" x2="1" y2="1">
      <stop offset="0" stop-color="var(--teal-mid)"/>
      <stop offset="0.45" stop-color="var(--teal-light)"/>
      <stop offset="0.7" stop-color="var(--teal-mid)"/>
      <stop offset="1" stop-color="var(--teal-deep)"/>
    </linearGradient>
    <radialGradient id="wash-sky" cx="0.4" cy="0.45" r="0.8">
      <stop offset="0" stop-color="var(--sky-pale)"/>
      <stop offset="1" stop-color="var(--sky-soft)"/>
    </radialGradient>

    <symbol id="icon-qa" viewBox="0 0 36 36">
      <title>Questions and answers</title>
      <path class="feature-icon" stroke="currentColor" d="M4 6 H26 V20 H14 L8 26 V20 H4 Z"/>
      <path class="feature-icon" stroke="currentColor" d="M29 12 H32 V27 H29 V32 L24 27 H15 V23"/>
    </symbol>
    <symbol id="icon-notes" viewBox="0 0 36 36">
      <title>Theory notes</title>
      <path class="feature-icon" stroke="currentColor" d="M8 3 H23 L29 9 V33 H8 Z M23 3 V9 H29"/>
      <path class="feature-icon" stroke="currentColor" d="M13 15 H24 M13 20 H24 M13 25 H20"/>
    </symbol>
    <symbol id="icon-tips" viewBox="0 0 36 36">
      <title>Tips and tricks</title>
      <path class="feature-icon" stroke="currentColor" d="M13 25 C13 20 8 18 8 12 A10 10 0 0 1 28 12 C28 18 23 20 23 25 Z"/>
      <path class="feature-icon" stroke="currentColor" d="M14 29 H22 M15 33 H21"/>
    </symbol>
    <symbol id="icon-previous" viewBox="0 0 36 36">
      <title>Previous years' reference questions</title>
      <path class="feature-icon" stroke="currentColor" d="M6 18 A12 12 0 1 0 10 9"/>
      <path class="feature-icon" stroke="currentColor" d="M10 3 V9 H4 M18 11 V18 L23 22"/>
    </symbol>
    <symbol id="icon-syllabus" viewBox="0 0 36 36">
      <title>Covers complete syllabus</title>
      <circle class="feature-icon" stroke="currentColor" cx="18" cy="18" r="14"/>
      <path class="feature-icon" stroke="currentColor" d="M11 18 L16 23 L25 13"/>
    </symbol>
  </defs>

  <rect class="sheet-frame" x="1" y="1" width="1401" height="1130"/>

  <!-- Option 1: bubbles cover -->
  <g class="cover cover-bubbles">
    <rect x="103" y="133" width="561" height="787" fill="url(#wash-teal)" role="img" aria-label="Teal watercolour wash background"/>
    <text class="serif title-serif" x="385" y="258" text-anchor="middle">Physics</text>

    <g class="feature-row features-light" aria-label="Book features">
      <use href="#icon-qa" x="251" y="296" width="36" height="36"/>
      <use href="#icon-notes" x="309" y="296" width="36" height="36"/>
      <use href="#icon-tips" x="367" y="296" width="36" height="36"/>
      <use href="#icon-previous" x="425" y="296" width="36" height="36"/>
      <use href="#icon-syllabus" x="483" y="296" width="36" height="36"/>
    </g>

    <circle class="bubble" cx="498" cy="533" r="62"/>
    <circle class="bubble" cx="350" cy="462" r="113"/>
    <circle class="bubble" cx="232" cy="697" r="95"/>
    <circle class="bubble" cx="465" cy="730" r="140"/>
    <circle class="bubble" cx="280" cy="847" r="63"/>
    <circle class="bubble" cx="182" cy="857" r="45"/>
    <circle class="bubble-white" cx="578" cy="857" r="51"/>
    <circle class="bubble-white" cx="400" cy="558" r="50"/>

    <text class="serif volume-label" x="353" y="460" text-anchor="middle" font-size="52">Volume</text>
    <text class="serif volume-label" x="352" y="502" text-anchor="middle" font-size="46">no</text>
    <text class="serif volume-label" x="403" y="590" text-anchor="middle" font-size="82">1</text>

    <text class="publisher" x="457" y="727" text-anchor="middle">VORLIN</text>
    <text class="publisher" x="457" y="757" text-anchor="middle">Education</text>
  </g>

  <!-- Option 2: diagonal bands cover -->
  <g class="cover cover-bands">
    <rect x="719" y="137" width="562" height="794" fill="url(#wash-sky)" role="img" aria-label="Pale blue textured paper background"/>
    <path class="band-lime" d="M1266,137 L1281,137 L1281,420 L1180,510 L1025,652 Q1095,575 1130,510 Q1195,400 1266,137 Z"/>
    <path class="band-cyan" d="M720,931 L1028,650 L1180,508 L1005,928 Z"/>

    <text class="title-sans" x="760" y="250">Physics</text>

    <g class="feature-row features-dark" aria-label="Book features">
      <use href="#icon-qa" x="764" y="300" width="36" height="36"/>
      <use href="#icon-notes" x="822" y="300" width="36" height="36"/>
      <use href="#icon-tips" x="880" y="300" width="36" height="36"/>
      <use href="#icon-previous" x="938" y="300" width="36" height="36"/>
      <use href="#icon-syllabus" x="996" y="300" width="36" height="36"/>
    </g>

    <text class="serif volume-label" x="762" y="597" font-size="62">Volume</text>
    <text class="serif volume-label" x="807" y="660" font-size="58">no 1</text>

    <text class="publisher" x="1164" y="878" text-anchor="middle">VORLIN</text>
    <text class="publisher" x="1164" y="906" text-anchor="middle">Education</text>
  </g>

  <text class="option-label" x="456" y="1001">Option 1</text>
  <text class="option-label" x="1083" y="985">Option 2</text>
</svg>
</body>
</html>
```